Corporate Design für Lieferant von Gastronomiebedarfsartikel
Zielgruppe
Belieferung von Restaurants Pizzerien mit Verpackungen (Pizzakartons usw, Verbrauchsmaterialinen( Servietten Spülmittel usw)
komplette Kücheneinrichtungen
Verkauf von Spülmaschinen, Porzellan Bestecken
Aufgabenstellung
Schlicht modern
Farbe des Logos:Rot, Schrift TRL weißer Hintergrund
Schrift Firmen Angaben im Briefkopf :grau anthrazit ( z. B. Name Adresse Email usw )
Design: neues junges Unternehmen
Ich habe einige Logos unserer Liefernaten hochgeladen: Porzellan: Vornalux , Grossküchengeräten: Rinaldo Ve, Servietten: Pelka, Spülmaschinen :Tarvo diese bitte auch mit angeben/ Logos daneben ( im Briefkopf )
Ich habe das alte Logo der Firma die ich unter meinem Namen weiterführen werde auch hochgeladen
Im Logo Lindhorst und Soberan sehen sie das Rot was ich mir als Farbe für das Logo wünsche

```html
<!DOCTYPE html>
<html lang="de">
<head>
<meta charset="utf-8">
<title>TRL Gastronomiebedarf – Corporate Design</title>
<link rel="stylesheet" href="https://fonts.googleapis.com/css2?family=Open+Sans:wght@400;600;800&display=swap">
<style>
  :root{
    --brand-red:#c0141f;
    --anthracite:#333333;
    --stage:#3b3b3b;
    --paper:#ffffff;
    --paper-soft:#f8f8f8;
    --text-grey:#4a4a4a;
    --partner-grey:#c4c8cc;
  }
  *{box-sizing:border-box;margin:0;padding:0}
  html,body{width:1096px;height:1200px;overflow:hidden}
  body{background:var(--stage);font-family:"Open Sans",Arial,sans-serif;color:var(--anthracite);position:relative}
  .sheet{position:absolute;background:var(--paper);box-shadow:0 4px 14px rgba(0,0,0,.35)}

  /* logo */
  .logo{display:inline-flex;flex-direction:column;align-items:flex-start;color:var(--brand-red);line-height:1}
  .logo-name{font-weight:800;letter-spacing:.02em}
  .logo-sub{font-weight:800}
  .logo-company{font-weight:600}
  .logo--inverse{color:#fff}

  /* business card front */
  .card-front{left:72px;top:51px;width:211px;height:329px;text-align:center;padding-top:40px}
  .card-front .logo{align-items:center}
  .card-front .logo-name{font-size:64px}
  .card-front .logo-sub{font-size:11px;margin-top:4px}
  .card-front .logo-company{font-size:7px;margin-top:3px;color:var(--anthracite)}
  .contact{font-size:8px;line-height:14px;color:var(--text-grey);margin-top:46px}
  .contact p+p{margin-top:10px}
  .web{font-size:8px;font-weight:800;color:var(--brand-red);position:absolute;bottom:22px;left:0;right:0}

  /* card backs */
  .card-back{left:72px;width:211px;height:329px;text-align:center;background:var(--paper-soft)}
  .services{list-style:none;font-size:10.5px;line-height:19.4px;padding-top:20px}
  .services li:nth-child(2){margin-top:-7px}
  .more{font-size:9px;font-weight:800;color:var(--brand-red);margin-top:14px}
  .partners{display:flex;justify-content:space-around;align-items:center;position:absolute;left:6px;right:6px;bottom:14px}
  .partner{font-size:8px;font-weight:800;color:var(--partner-grey)}
  .card-back--light{top:431px}
  .card-back--red{top:808px}
  .card-back--red .red-field{background:var(--brand-red);height:255px;border-bottom:3px solid var(--anthracite)}
  .card-back--red .services{color:#fff;font-weight:800;padding-top:16px}
  .card-back--red .more{margin-top:16px}

  /* letterheads */
  .letter{left:374px;width:359px;height:508px;background:var(--paper-soft);overflow:hidden}
  .fold{position:absolute;left:0;top:180px;width:16px;height:1px;background:#9a9a9a}
  .letter-a{top:54px}
  .letter-a .logo{position:absolute;left:34px;top:30px}
  .letter-a .logo-name{font-size:38px}
  .letter-a .logo-sub{font-size:6px;margin-top:2px}
  .letter-a .url{position:absolute;right:17px;top:76px;font-size:7px;font-weight:600}
  .letter-a .footer{position:absolute;right:17px;top:432px;text-align:right;font-size:5px;line-height:8.5px;color:var(--text-grey)}
  .letter-a .footer .more{font-size:6.5px;font-weight:600;margin:2px 0 6px}
  .letter-a .fine{font-size:3px;line-height:6.5px}
  .letter-a .partner-stack{position:absolute;left:34px;top:430px;display:flex;flex-direction:column;gap:7px}
  .partner-stack .partner{font-size:5.5px;color:var(--anthracite)}
  .letter-b{top:629px}
  .letter-b .aside{position:absolute;right:17px;top:34px;width:110px;text-align:center}
  .letter-b .logo{align-items:center}
  .letter-b .logo-name{font-size:34px}
  .letter-b .logo-sub{font-size:5.5px;margin-top:2px}
  .letter-b .services{font-size:5px;line-height:12.4px;padding-top:12px}
  .letter-b .services li:nth-child(2){margin-top:-5px}
  .letter-b .more{font-size:6.5px;font-weight:600;margin-top:6px}
  .letter-b .partner-col{display:flex;flex-direction:column;gap:22px;margin-top:16px}
  .letter-b .partner{font-size:7px}
  .letter-b .fine{font-size:3.6px;line-height:6px;color:var(--text-grey);margin-top:26px}
  .letter-b .fine p+p{margin-top:5px}
  .letter-b .url{position:absolute;right:17px;top:484px;font-size:6.5px;font-weight:800;color:var(--brand-red);white-space:nowrap}

  /* logo tiles */
  .tile{left:792px;width:233px;display:flex;align-items:center;justify-content:center}
  .tile .logo-name{font-size:84px}
  .tile .logo-sub{font-size:13px;margin-top:4px}
  .tile .logo-company{font-size:8px;margin-top:3px;color:var(--anthracite)}
  .tile-red{top:59px;height:160px}
  .tile-grey{top:241px;height:157px}
  .tile-grey .logo-sub{background:#707070;color:#fff;padding:2px 6px}
  .tile-black{top:422px;height:158px;background:#000}
  .tile-black .logo-company{color:#fff}

  /* colour swatches */
  .swatch{position:absolute;width:217px;height:93px}
  .swatch-red{left:801px;top:934px;background:var(--brand-red)}
  .swatch-dark{left:803px;top:1042px;background:var(--anthracite)}
</style>
</head>
<body>

<section class="sheet card-front" aria-label="Visitenkarte Vorderseite">
  <div class="logo">
    <span class="logo-name">TRL</span>
    <span class="logo-sub">Gastronomiebedarf</span>
    <span class="logo-company">Brenner-Kahlert GmbH</span>
  </div>
  <div class="contact">
    <p>Vorname Nachname</p>
    <p>Lindenpfad 12<br>50999 Musterstadt (Nord)</p>
    <p>Tel: 01234/56780 | Fax: 01234/56781<br>kontakt@gastro-brenner.example</p>
  </div>
  <p class="web">www.gastro-brenner.example</p>
</section>

<section class="sheet card-back card-back--light" aria-label="Visitenkarte Rückseite hell">
  <ul class="services">
    <li>Großküchen</li><li>Planung-Verkauf-Service</li><li>Pizzatechnik</li><li>Kühlgeräte</li><li>Objektmobilar</li><li>Bestecke</li><li>Porzellan</li><li>Servientten</li><li>Tischwäsche</li><li>Kochgeschirr</li><li>Außer-Haus-Verpackungen</li><li>Reiniger / Hygiene</li>
  </ul>
  <p class="more">und vieles mehr...</p>
  <div class="partners"><span class="partner">Rinaldo Ve</span><span class="partner">Pelka</span><span class="partner">Vornalux</span><span class="partner">Tarvo</span></div>
</section>

<section class="sheet card-back card-back--red" aria-label="Visitenkarte Rückseite rot">
  <div class="red-field">
    <ul class="services">
      <li>Großküchen</li><li>Planung-Verkauf-Service</li><li>Pizzatechnik</li><li>Kühlgeräte</li><li>Objektmobilar</li><li>Bestecke</li><li>Porzellan</li><li>Servientten</li><li>Tischwäsche</li><li>Kochgeschirr</li><li>Außer-Haus-Verpackungen</li><li>Reiniger / Hygiene</li>
    </ul>
  </div>
  <p class="more">und vieles mehr...</p>
  <div class="partners"><span class="partner">Rinaldo Ve</span><span class="partner">Pelka</span><span class="partner">Vornalux</span><span class="partner">Tarvo</span></div>
</section>

<section class="sheet letter letter-a" aria-label="Briefbogen quer">
  <div class="logo"><span class="logo-name">TRL</span><span class="logo-sub">Gastronomiebedarf</span></div>
  <p class="url">www.gastro-brenner.example</p>
  <span class="fold"></span>
  <div class="partner-stack"><span class="partner">Rinaldo Ve</span><span class="partner">Pelka</span><span class="partner">Vornalux</span><span class="partner">Tarvo</span></div>
  <div class="footer">
    <p>Großküchen Planung-Verkauf-Service | Pizzatechnik | Kühlgeräte | Objektmobilar</p>
    <p>Bestecke | Porzellan | Servientten | Tischwäsche | Kochgeschirr</p>
    <p>Außer-Haus-Verpackungen | Reiniger | Hygiene</p>
    <p class="more">und vieles mehr...</p>
    <div class="fine">
      <p>Geschäftsführer | Lindenpfad 12 | 50999 Musterstadt (Nord) | Tel: 01234/56780 | Fax: 01234/56781 | kontakt@gastro-brenner.example</p>
      <p>Juristischer Sitz / Verwaltung: Straße 0 | 00000 Stadt | Gerichtsstand Musterstadt | USt-Id-Nr. DE 000000000</p>
      <p>Bankverbindung: Bank | IBAN DE00 0000 0000 0000 0000 00 | BIC AAAAAAAAAAA</p>
    </div>
  </div>
</section>

<section class="sheet letter letter-b" aria-label="Briefbogen mit Seitenspalte">
  <span class="fold"></span>
  <div class="aside">
    <div class="logo"><span class="logo-name">TRL</span><span class="logo-sub">Gastronomiebedarf</span></div>
    <ul class="services">
      <li>Großküchen</li><li>Planung-Verkauf-Service</li><li>Pizzatechnik</li><li>Kühlgeräte</li><li>Objektmobilar</li><li>Bestecke</li><li>Porzellan</li><li>Servientten</li><li>Tischwäsche</li><li>Kochgeschirr</li><li>Außer-Haus-Verpackungen</li><li>Reiniger / Hygiene</li>
    </ul>
    <p class="more">und vieles mehr...</p>
    <div class="partner-col"><span class="partner">Rinaldo Ve</span><span class="partner">Pelka</span><span class="partner">Vornalux</span><span class="partner">Tarvo</span></div>
    <div class="fine">
      <p>Geschäftsführer<br>Lindenpfad 12 | 50999 Musterstadt<br>(Nord)<br>Tel: 01234/56780 | Fax: 01234/56781<br>kontakt@gastro-brenner.example</p>
      <p>Juristischer Sitz / Verwaltung: Straße 0 | 00000 Stadt<br>Gerichtsstand Musterstadt<br>USt-Id-Nr. DE 000000000</p>
      <p>Bankverbindung:<br>Bank | IBAN DE00 0000 0000 0000 0000 00<br>BIC AAAAAAAAAAA</p>
    </div>
  </div>
  <p class="url">www.gastro-brenner.example</p>
</section>

<section class="sheet tile tile-red" aria-label="Logo Variante Rot">
  <div class="logo"><span class="logo-name">TRL</span><span class="logo-sub">Gastronomiebedarf</span><span class="logo-company">Brenner-Kahlert GmbH</span></div>
</section>
<section class="sheet tile tile-grey" aria-label="Logo Variante Grau">
  <div class="logo"><span class="logo-sub">Gastronomiebedarf</span><span class="logo-name">TRL</span><span class="logo-company">Brenner - Kahlert GmbH</span></div>
</section>
<section class="sheet tile tile-black" aria-label="Logo Variante negativ">
  <div class="logo logo--inverse"><span class="logo-name">TRL</span><span class="logo-sub">Gastronomiebedarf</span><span class="logo-company">Brenner-Kahlert GmbH</span></div>
</section>

<div class="swatch swatch-red" aria-label="Hausfarbe Rot"></div>
<div class="swatch swatch-dark" aria-label="Hausfarbe Anthrazit"></div>

</body>
</html>
```